Landing page for a cyber security service provider called 'Lumen Grove'

The client is a new cyber security company in need of a website landing page at lumengrove.example.

Their visual identity is modern, playful, clean and uncluttered and represents innovation, connectivity and approachability.

The company logo is provided in black (attached) but the client is open to changing the colour to align with the new website design.

The landing page needs to contain:
- A call to action with a 'Get Started' button
-Links to blank 'How it works', 'Products', 'Pricing', 'About Us' and 'Contact Us' pages (that we'll fill out later)

Target Market(s)

Medium to large businesses who probably don't understand cyber / cyber security but need their business to be protected.

Industry/Entity Type

Cyber Security

Coding

Coded - Design and coding required

Number of Pages Required

1 page

Font styles to use
Sans Serif
Other font styles liked:
• Helvetica

Requirements
Nice to have
• Hero banner at the top of the landing page.
Should not have
• Should not look like a traditional cyber / cyber security design (eg no dark blue/ black, red/black colour combinations). Please no military styles (eg no shields, cannons, swords, guns)

```html
<!DOCTYPE html>
<html lang="en">
<head>
<meta charset="utf-8">
<title>Lumen Grove — Cyber Security</title>
<link href="https://fonts.googleapis.com/css2?family=Arimo:wght@400;500;600;700&display=swap" rel="stylesheet">
<style>
:root{
  --yellow:#FDBE2C;
  --orange:#FF8412;
  --pink:#FF6F91;
  --magenta:#E2337F;
  --purple:#7A12D8;
  --violet:#A60CC8;
  --lime:#8DD30F;
  --ink:#1a1a1a;
  --grey-text:#444;
  --card-grey:#E8E8EA;
  --page:#F5F5F6;
  --field:#ECECEE;
  --white:#ffffff;
}
*{box-sizing:border-box;margin:0;padding:0}
html,body{width:1200px;height:3790px;overflow:hidden}
body{font-family:"Arimo",Helvetica,Arial,sans-serif;background:var(--page);color:var(--ink);position:relative}
.abs{position:absolute}
a{color:inherit;text-decoration:none}

/* logo */
.logo{display:flex;align-items:center;gap:14px;font-weight:700;color:var(--ink)}
.logo-dot{width:34px;height:34px;border-radius:50%;background:var(--ink)}
.logo-name{font-size:44px;letter-spacing:-0.5px}

/* hero */
.hero{left:0;top:0;width:1200px;height:613px;background:var(--yellow)}
.hero .logo{position:absolute;left:68px;top:30px}
.nav{position:absolute;left:579px;top:52px;display:flex;gap:24px;font-size:13.5px;font-weight:700;color:var(--white)}
.nav a.active{color:var(--ink)}
.hero-title{position:absolute;left:70px;top:160px;color:var(--white);font-weight:700;font-size:88px;line-height:76px;letter-spacing:-0.5px}
.hero-sub{position:absolute;left:86px;top:322px;color:var(--white);font-weight:700;font-size:48px}
.hero-text{position:absolute;left:86px;top:388px;width:420px;color:var(--white);font-size:15.5px;line-height:22px}
.btn-hero{position:absolute;left:87px;top:472px;width:185px;height:47px;background:var(--white);color:var(--ink);font-weight:700;font-size:15px;display:flex;align-items:center;justify-content:center}
.hero-art{position:absolute;left:600px;top:118px;width:600px;height:495px;background:linear-gradient(135deg,#7FF0F2 0%,#3ED3E0 40%,#FF8FB8 75%,#FFB25A 100%);border-radius:18px 0 0 0;opacity:.85}

/* section heads */
.grad-title{font-weight:700;background:linear-gradient(90deg,#FF7A1A,var(--magenta));-webkit-background-clip:text;background-clip:text;color:transparent;text-align:center;position:absolute;left:0;width:1200px}
.lead{position:absolute;text-align:center;color:var(--grey-text)}

/* about */
.about-card{position:absolute;top:837px;width:525px;height:145px;background:var(--pink);border-radius:18px;padding:18px 26px;color:var(--white)}
.about-card h3{font-size:23px;font-weight:700;margin-bottom:8px}
.about-card p{font-size:18px;line-height:23px;opacity:.85}

/* how it works */
.how-panel{left:88px;top:1128px;width:992px;height:582px;background:var(--white)}
.how-img{position:absolute;top:1142px;width:240px;height:513px}
.how-label{position:absolute;top:1678px;width:240px;text-align:center;font-size:16.5px;font-weight:700}

/* services */
.service{position:absolute;top:1843px;width:301px;height:244px;background:var(--card-grey);border-radius:32px;text-align:center;padding-top:36px}
.service.hot{background:var(--yellow)}
.service svg{width:56px;height:56px}
.service h3{font-size:28px;font-weight:700;margin:12px 0 10px}
.service p{font-size:16px;line-height:24px;color:#333;padding:0 26px}

/* stats */
.stats{left:0;top:2160px;width:1200px;height:140px;background:var(--orange)}
.stat{position:absolute;top:2190px;color:var(--white);display:flex;align-items:flex-start;gap:12px}
.stat-icon{width:42px;height:38px;border-radius:8px;margin-top:16px}
.stat-num{font-size:72px;font-weight:700;line-height:66px}
.stat-cap{font-size:13px;font-weight:700;margin-top:2px}

/* pricing */
.plan{position:absolute;top:2421px;width:301px;height:360px;background:#EDEDEF;text-align:center;padding-top:24px;color:#333}
.plan.featured{background:linear-gradient(160deg,#8A0FD8,#5B1CF0);color:var(--white);border-radius:6px}
.price{font-size:52px;font-weight:700;color:var(--purple)}
.price small{font-size:15px;font-weight:400;color:#333}
.plan.featured .price,.plan.featured .price small{color:var(--white)}
.plan h3{font-size:23px;font-weight:700;color:#555;margin:8px 0 14px}
.plan.featured h3{color:var(--white)}
.plan .desc{font-size:13px;line-height:18px;padding:0 26px;margin-bottom:16px}
.plan ul{list-style:none;font-size:13px;line-height:24.5px}
.btn-plan{display:inline-block;margin-top:10px;width:154px;height:40px;line-height:40px;font-size:13.5px;font-weight:700;color:var(--white);background:linear-gradient(90deg,#FF7A1A,#FF3F6A)}
.plan.featured .btn-plan{background:var(--lime)}

/* cta */
.cta{left:66px;top:2830px;width:1065px;height:326px;background:var(--violet);overflow:hidden}
.cta-wedge{position:absolute;left:0;top:0;width:1065px;height:326px;background:#E5A8F0;clip-path:polygon(0 0,315px 0,440px 326px,0 326px)}
.cta-art{position:absolute;left:20px;top:10px;width:420px;height:300px;border-radius:50%;background:radial-gradient(circle at 45% 40%,#D25BFF,#7E3BE6 60%,transparent 72%)}
.cta h2{position:absolute;right:40px;top:65px;text-align:right;color:var(--white);font-size:45px;line-height:44px;font-weight:700}
.cta p{position:absolute;right:46px;top:182px;color:var(--white);font-size:16px}
.btn-cta{position:absolute;right:50px;top:228px;width:237px;height:58px;background:linear-gradient(90deg,#FF7A1A,#FF4A5A);color:var(--white);font-size:26px;font-weight:700;display:flex;align-items:center;justify-content:center}

/* contact */
.contact-art{left:870px;top:3230px;width:330px;height:345px;background:radial-gradient(circle at 60% 55%,rgba(255,220,170,.55),rgba(230,210,255,.35) 55%,transparent 75%)}
.block-title{position:absolute;font-size:22px;font-weight:700}
.field{position:absolute;background:var(--field);border-radius:3px;color:#aaa;font-size:13px;padding:12px 16px}
.btn-send{position:absolute;left:91px;top:3488px;width:156px;height:40px;background:linear-gradient(90deg,#FF5A1A,#FF3F55);color:var(--white);font-size:12.5px;font-weight:700;display:flex;align-items:center;justify-content:center}
.info-head{position:absolute;left:712px;display:flex;align-items:center;gap:10px;font-weight:700;font-size:17px;color:#444}
.info-val{position:absolute;left:712px;font-size:14px;color:#222}
.social{position:absolute;top:3488px;width:22px;height:22px;border:1.5px solid #666;border-radius:50%}

/* footer */
.footer{left:0;top:3583px;width:1200px;height:207px;background:var(--yellow)}
.footer .logo{position:absolute;left:0;width:1200px;justify-content:center;top:38px}
.footer-links{position:absolute;top:3718px;left:0;width:1200px;text-align:center;font-size:14px;color:#222}
.footer-links span{margin:0 12px}
.copy{position:absolute;top:3760px;left:0;width:1200px;text-align:center;font-size:11.5px;color:#222}
</style>
</head>
<body>

<!-- hero -->
<header class="abs hero">
  <div class="logo"><span class="logo-dot"></span><span class="logo-name">Lumen Grove</span></div>
  <nav class="nav">
    <a class="active" href="#">Home</a><a href="#">About Us</a><a href="#">Products</a><a href="#">Pricing</a><a href="#">How it works</a><a href="#">Contact Us</a>
  </nav>
  <h1 class="hero-title">We Protect<br>The World's</h1>
  <div class="hero-sub">Most Sensitive Data</div>
  <p class="hero-text">Lorem ipsum dolor sit amet, consectetur adipiscing elit, sed do eiusmod tempor incididunt ut labore et dolore magna aliqua. accumsan lacus vel facilisis.</p>
  <a class="btn-hero" href="#">GET STARTED</a>
  <div class="hero-art" role="img" aria-label="3D illustration of a hooded figure wearing a visor amid floating holographic screens, a padlock and a puzzle piece"></div>
</header>

<!-- about -->
<h2 class="grad-title" style="top:660px;font-size:56px">About Us</h2>
<p class="lead" style="left:70px;width:1060px;top:736px;font-size:22px;line-height:29px">Lorem ipsum dolor sit amet, consectetur adipiscing elit, sed do eiusmod tempor incididunt ut labore et dolore magna aliqua. accumsan lacus vel facilisis.</p>
<div class="about-card" style="left:65px">
  <h3>Highly Professional Members</h3>
  <p>Lorem ipsum dolor sit amet, consectetur adipiscing elit, sed do eiusmod tempor incididunt ut labore et dolore magna aliqua.</p>
</div>
<div class="about-card" style="left:606px">
  <h3>Infrastructure Integration Technology</h3>
  <p>Lorem ipsum dolor sit amet, consectetur adipiscing elit, sed do eiusmod tempor incididunt ut labore et dolore magna aliqua.</p>
</div>

<!-- how it works -->
<h2 class="grad-title" style="top:1020px;font-size:54px">How it works</h2>
<p class="lead" style="left:0;width:1200px;top:1090px;font-size:21px">Lorem ipsum dolor sit amet, consectetur&nbsp; adipiscing elit, sed do eiusmod tempor.</p>
<div class="abs how-panel"></div>
<div class="how-img" style="left:112px;background:linear-gradient(160deg,#1E3E8C,#2E86D6 50%,#F2A23A)" role="img" aria-label="Illustration of a padlock on a geometric panel among swirling colourful shapes"></div>
<div class="how-img" style="left:355px;background:linear-gradient(180deg,#4A2FB5,#C9A6F5 50%,#3B1F9A)" role="img" aria-label="Illustration of a glowing geodesic dome window"></div>
<div class="how-img" style="left:598px;background:linear-gradient(170deg,#2F6CE0,#8FE0FF 55%,#1E4FC8)" role="img" aria-label="Illustration of a workspace with laptop beside a window with floating warning signs"></div>
<div class="how-img" style="left:841px;background:linear-gradient(180deg,#E7C9FF,#8A4AD8 45%,#2E1660)" role="img" aria-label="Illustration of a figure standing over a winding purple landscape"></div>
<div class="how-label" style="left:112px">Infrastructure Security</div>
<div class="how-label" style="left:355px">Data Security</div>
<div class="how-label" style="left:598px">Cloud-native Security</div>
<div class="how-label" style="left:841px">Application Security</div>

<!-- services -->
<h2 class="grad-title" style="top:1744px;font-size:42px">Our Service Products</h2>
<p class="lead" style="left:0;width:1200px;top:1796px;font-size:19px">Lorem ipsum dolor sit amet, consectetur adipiscing elit, do eiusmod.</p>
<div class="service" style="left:109px">
  <svg viewBox="0 0 56 56" fill="none" stroke="#111" stroke-width="3"><circle cx="28" cy="28" r="18"/><circle cx="28" cy="24" r="6"/><path d="M28 30v8"/></svg>
  <h3>Cyber Security</h3>
  <p>Lorem ipsum dolor sit amet, consectetur adipiscing elit, sed eiusmod amet elit.</p>
</div>
<div class="service" style="left:451px">
  <svg viewBox="0 0 56 56" fill="none" stroke="#111" stroke-width="3.5"><circle cx="28" cy="28" r="24"/><path d="M16 29l8 8 17-18"/></svg>
  <h3>Data Protection</h3>
  <p>Lorem ipsum dolor sit amet, consectetur adipiscing elit, sed eiusmod amet elit.</p>
</div>
<div class="service hot" style="left:791px">
  <svg viewBox="0 0 56 56" fill="none" stroke="#111" stroke-width="3"><path d="M18 24v-7a10 10 0 0 1 20 0v7"/><rect x="10" y="24" width="36" height="24" rx="4"/><path d="M18 36h20"/></svg>
  <h3>Data Privacy</h3>
  <p>Lorem ipsum dolor sit amet, consectetur adipiscing elit, sed eiusmod amet elit.</p>
</div>

<!-- stats -->
<div class="abs stats"></div>
<div class="stat" style="left:115px"><span class="stat-icon" style="background:#C7E6FF"></span><div><div class="stat-num">12</div><div class="stat-cap">Years Experience</div></div></div>
<div class="stat" style="left:378px"><span class="stat-icon" style="background:#5FB8F5;width:36px"></span><div><div class="stat-num">95</div><div class="stat-cap">Customer Satisfaction</div></div></div>
<div class="stat" style="left:650px"><span class="stat-icon" style="background:#6E7BF0;width:36px;border-radius:50%"></span><div><div class="stat-num">38</div><div class="stat-cap">Team Members</div></div></div>
<div class="stat" style="left:882px"><span class="stat-icon" style="background:#A9B6FF;width:40px;border-radius:50%"></span><div><div class="stat-num">321</div><div class="stat-cap">Porject Complete</div></div></div>

<!-- pricing -->
<p class="lead" style="left:0;width:1200px;top:2335px;font-size:19px">Pricing Plan</p>
<h2 class="grad-title" style="top:2356px;font-size:42px">Find The Plan That’s Right For You</h2>
<div class="plan" style="left:109px">
  <div class="price">$25<small>/ MONTHLY</small></div>
  <h3>Basic Plan</h3>
  <p class="desc">Lorem ipsum dolor sit amet, consectetur adipiscing elit, sed eiusmod amet elit.</p>
  <ul><li>30 Days Product Testing</li><li>Upgrade Anytime Protection</li><li>500 Malware Removal</li><li>Configure Software One Time</li><li>24/7 Live Assistance</li></ul>
  <a class="btn-plan" href="#">CHOOSE PLAN</a>
</div>
<div class="plan featured" style="left:451px">
  <div class="price">$55<small>/ MONTHLY</small></div>
  <h3>Standard Plan</h3>
  <p class="desc">Lorem ipsum dolor sit amet, consectetur adipiscing elit, sed eiusmod amet elit.</p>
  <ul><li>30 Days Product Testing</li><li>Upgrade Anytime Protection</li><li>500 Malware Removal</li><li>Configure Software One Time</li><li>24/7 Live Assistance</li></ul>
  <a class="btn-plan" href="#">CHOOSE PLAN</a>
</div>
<div class="plan" style="left:790px">
  <div class="price">$105<small>/ MONTHLY</small></div>
  <h3>Premium Plan</h3>
  <p class="desc">Lorem ipsum dolor sit amet, consectetur adipiscing elit, sed eiusmod amet elit.</p>
  <ul><li>30 Days Product Testing</li><li>Upgrade Anytime Protection</li><li>500 Malware Removal</li><li>Configure Software One Time</li><li>24/7 Live Assistance</li></ul>
  <a class="btn-plan" href="#">CHOOSE PLAN</a>
</div>

<!-- call to action -->
<section class="abs cta">
  <div class="cta-wedge"></div>
  <div class="cta-art" role="img" aria-label="Illustration of a purple wireframe globe with orbit rings and clouds"></div>
  <h2>A better secure network for<br>safer workplace</h2>
  <p>Lorem ipsum dolor sit amet, consectetur adipiscing elit, do eiusmod.</p>
  <a class="btn-cta" href="#">GET STARTED</a>
</section>

<!-- contact -->
<div class="abs contact-art" role="img" aria-label="Soft 3D illustration of a hand reaching toward floating cubes"></div>
<h3 class="block-title" style="left:91px;top:3195px">Write Us</h3>
<div class="field" style="left:91px;top:3241px;width:268px;height:41px">Name</div>
<div class="field" style="left:372px;top:3241px;width:265px;height:41px">Email Address</div>
<div class="field" style="left:91px;top:3296px;width:268px;height:41px">Phone</div>
<div class="field" style="left:372px;top:3296px;width:265px;height:41px">Subject</div>
<div class="field" style="left:91px;top:3352px;width:546px;height:122px">Message</div>
<a class="btn-send" href="#">SEND US A MESSAGE</a>

<h3 class="block-title" style="left:709px;top:3195px">Contact Us</h3>
<p class="abs" style="left:712px;top:3238px;width:400px;font-size:16px;line-height:24px;color:#333">Lorem ipsum dolor sit amet, consectetur adipiscing elit, sed eiusmod amet elit.</p>
<div class="info-head" style="top:3307px"><svg width="20" height="20" viewBox="0 0 20 20" fill="none" stroke="#222" stroke-width="2"><path d="M10 19s6-6 6-11a6 6 0 0 0-12 0c0 5 6 11 6 11z"/><circle cx="10" cy="8" r="2"/></svg>Address</div>
<div class="info-val" style="top:3338px">Plaza x , xy floor, street, xyz</div>
<div class="info-head" style="top:3363px"><svg width="20" height="20" viewBox="0 0 20 20" fill="#222"><path d="M4 2l4 1 1 4-2 2a11 11 0 0 0 4 4l2-2 4 1 1 4-2 2C8 18 2 12 2 4z"/></svg>Phone</div>
<div class="info-val" style="top:3394px">+123-456-7890</div>
<div class="info-head" style="top:3418px"><svg width="24" height="18" viewBox="0 0 24 18" fill="none" stroke="#222" stroke-width="2"><rect x="1" y="1" width="22" height="16" rx="1"/><path d="M1 2l11 8 11-8"/></svg>Email</div>
<div class="info-val" style="top:3450px">hello@lumengrove.example</div>
<span class="social" style="left:714px"></span>
<span class="social" style="left:746px"></span>
<span class="social" style="left:779px"></span>
<span class="social" style="left:812px"></span>

<!-- footer -->
<footer class="abs footer">
  <div class="logo"><span class="logo-dot"></span><span class="logo-name">Lumen Grove</span></div>
</footer>
<div class="footer-links"><a href="#">About Us</a><span>|</span><a href="#">Terms and conditions</a><span>|</span><a href="#">privacy policy</a><span>|</span><a href="#">Contact Us</a></div>
<div class="copy">Copyright © 2024 Lumen Grove. all rights reserved.</div>

</body>
</html>
```